TALBRIN ELEVATOR CORP

LOOKING FOR BLACK MATTE BACKGROUND WITH GLOSS DESIGN
NEED RAISED UV ON LOGO AND LETTERING , WITH ROUNDED CORNERS AND COLORED EDGES ( FLOURECENT BLUE)

```html
<!DOCTYPE html>
<html lang="en">
<head>
<meta charset="utf-8">
<title>Talbrin Elevator Corp – Business Card</title>
<link rel="stylesheet" href="https://fonts.googleapis.com/css2?family=Exo+2:wght@400;800&family=Montserrat:wght@600&display=swap">
<style>
  :root {
    --page-bg: #d9dadc;
    --card-bg: #121212;
    --edge-blue: #2a6db5;
    --name-blue: #2f7cc4;
    --accent-green: #4fa447;
    --text-white: #f4f4f4;
    --mark-blue: #3a7fc8;
  }
  * { margin: 0; padding: 0; box-sizing: border-box; }
  html, body {
    width: 1200px; height: 706px; overflow: hidden;
    background: var(--page-bg);
  }
  .canvas { position: relative; width: 1200px; height: 706px; }
  .card {
    position: absolute; top: 220px;
    width: 474px; height: 270px;
    background: var(--card-bg);
    border: 3px solid var(--edge-blue);
    border-radius: 20px;
    overflow: hidden;
    font-family: "Exo 2", sans-serif;
    color: var(--text-white);
  }
  .card--front { left: 91px; }
  .card--back { left: 635px; }

  .wordmark {
    position: absolute;
    font-family: "Exo 2", sans-serif;
    font-weight: 800;
    color: var(--text-white);
    font-size: 31px;
    line-height: 34px;
    letter-spacing: 0.5px;
  }
  .card--front .wordmark { left: 17px; top: 12px; }
  .wordmark .wordmark__line { display: block; }
  .card--front .wordmark__line--indent { padding-left: 40px; }
  .card--back .wordmark { left: 228px; top: 131px; width: 230px; text-align: center; }

  .holder-name {
    position: absolute; left: 58px; top: 128px;
    font-family: "Montserrat", sans-serif; font-weight: 600;
    font-size: 24px; color: var(--name-blue); letter-spacing: 0.3px;
  }
  .holder-title {
    position: absolute; left: 58px; top: 153px;
    font-size: 13px; font-weight: 400;
  }
  .title-rule {
    position: absolute; left: 126px; right: 0; top: 162px;
    height: 1px; background: var(--accent-green);
  }
  .contact-list { position: absolute; left: 58px; top: 178px; list-style: none; }
  .contact-list li {
    display: flex; align-items: center; gap: 5px;
    height: 16.5px; font-size: 13.5px;
  }
  .contact-list svg { width: 13px; height: 13px; flex: none; }
  .address {
    position: absolute; left: 58px; top: 237px;
    font-size: 13px; color: var(--accent-green);
  }

  .established {
    position: absolute; left: 228px; top: 111px; width: 230px;
    text-align: center; font-size: 13px; letter-spacing: 0.3px;
  }
  .brand-dot {
    position: absolute; left: 55px; top: 107px;
    width: 146px; height: 146px; border-radius: 50%;
    background: var(--mark-blue);
  }
</style>
</head>
<body>
<main class="canvas">
  <section class="card card--front" aria-label="Business card front">
    <h1 class="wordmark">
      <span class="wordmark__line">TALBRIN</span>
      <span class="wordmark__line">ELEVATOR</span>
      <span class="wordmark__line wordmark__line--indent">CORP</span>
    </h1>
    <p class="holder-name">NOLAN BRASKE</p>
    <p class="holder-title">President</p>
    <div class="title-rule"></div>
    <ul class="contact-list">
      <li>
        <svg viewBox="0 0 16 16" aria-hidden="true" fill="none" stroke="var(--name-blue)" stroke-width="1.3">
          <circle cx="8" cy="8" r="6.8"/>
          <path d="M5.3 4.6l1.4-.3.8 1.8-.9.8a5 5 0 0 0 2.5 2.5l.8-.9 1.8.8-.3 1.4c-3 .3-6.3-3-6.1-6.1z"/>
        </svg>
        (555) 014-2867
      </li>
      <li>
        <svg viewBox="0 0 16 16" aria-hidden="true" fill="none" stroke="var(--name-blue)" stroke-width="1.3">
          <rect x="1" y="3" width="14" height="10" rx="1"/>
          <path d="M1 3l7 6 7-6M1 13l5-5M15 13l-5-5"/>
        </svg>
        talbrinelevator@example.com
      </li>
      <li>
        <svg viewBox="0 0 16 16" aria-hidden="true" fill="none" stroke="var(--name-blue)" stroke-width="1.3">
          <circle cx="8" cy="8" r="6.8"/>
          <ellipse cx="8" cy="8" rx="3" ry="6.8"/>
          <path d="M1.2 8h13.6M2.3 4.5h11.4M2.3 11.5h11.4"/>
        </svg>
        www.talbrinelevatorny.com
      </li>
    </ul>
    <p class="address">2215 Halden Ave, Bronx 10460</p>
  </section>

  <section class="card card--back" aria-label="Business card back">
    <div class="brand-dot" aria-hidden="true"></div>
    <p class="established">ESTABLISHED 1978</p>
    <h2 class="wordmark">
      <span class="wordmark__line">TALBRIN</span>
      <span class="wordmark__line">ELEVATOR</span>
      <span class="wordmark__line">CORP</span>
    </h2>
  </section>
</main>
</body>
</html>
```